Redesign Website

I currently have a website www.kelvaromotionrx.com that I would like to have redesigned for esthetics and design limitations with the present platform. I will provide my logo, background logo (attached) , current site, foundation grip PSD.zip (attached) and a questionnaire (attached) from a web design company to provide the input to have an impressive site that pleases the eyes and makes an impact. I would also like the site to be mobile friendly.

IMPORTANT:
- The final PSD must include:
o Homepage Mockup
o Internal Pages Mockup
o Mobile site mockup
o Fonts files used in mockup

Final website will be responsive, using the Foundation Framework. Attached you will find a PSD of the Foundation grid – please use this and include with your final PSD. Here is a link for reference:
http://plimtex.com/article/1053/foundation-s-grid-and-photoshop-what-you-

Target Market(s)

Patients for physical therapy

Industry/Entity Type

It Company

Requirements
Must have
• Pages included in the present site. Photos and design should change.
Nice to have
• Should provide information necessary for patients to schedule an appointment
Should not have
• Should not be difficult to read.

```html
<!DOCTYPE html>
<html lang="en">
<head>
<meta charset="utf-8">
<title>Kelvaro Motion Physical Therapy</title>
<link rel="stylesheet" href="https://fonts.googleapis.com/css2?family=Open+Sans:wght@400;600;700&family=Source+Sans+3:wght@300;400;600&display=swap">
<style>
:root{
  --red:#c4272b;
  --red-dark:#9e1d21;
  --orange:#e8582a;
  --peach:#f6b894;
  --cream:#fbf4ee;
  --text:#6b6b6b;
  --heading:#c4272b;
  --white:#ffffff;
  --footer:#fdf3d6;
}
*{box-sizing:border-box;margin:0;padding:0}
html,body{width:1200px;height:3396px;overflow:hidden}
body{font-family:"Open Sans",Arial,sans-serif;color:var(--text);background:var(--white);position:relative;font-size:15px;line-height:1.6}
.wrap{position:absolute;left:110px;width:980px}
h1,h2,h3{font-family:"Source Sans 3","Open Sans",sans-serif;font-weight:400;color:var(--heading)}

/* header */
.site-header{position:absolute;top:0;left:0;width:1200px;height:120px;z-index:3}
.brand{position:absolute;left:112px;top:30px;display:flex;align-items:center;gap:12px}
.brand-mark{width:52px;height:52px;border-radius:50%;background:var(--orange)}
.brand-name{font-family:"Source Sans 3",sans-serif;font-size:34px;font-weight:600;color:var(--red);line-height:1}
.header-phone{position:absolute;left:680px;top:20px;font-size:20px;color:var(--red);font-weight:600;display:flex;gap:8px;align-items:center}
.appt-btn{position:absolute;left:860px;top:18px;background:var(--red);color:var(--white);font-size:12px;font-weight:700;padding:6px 18px;letter-spacing:.5px}
.main-nav{position:absolute;left:650px;top:72px;display:flex;gap:36px;font-size:18px;color:#444}
.main-nav .active{color:var(--red);border-bottom:3px solid var(--orange);padding-bottom:4px}

/* hero */
.hero{position:absolute;top:0;left:0;width:1200px;height:700px;background:linear-gradient(180deg,#ffffff 0%,#fbf1ea 100%);overflow:hidden}
.hero-photo{position:absolute;left:90px;top:110px;width:470px;height:490px;background:radial-gradient(ellipse at 50% 40%,#f3d1b9 0%,#e9b48f 45%,#f7e5d6 80%)}
.hero-band{position:absolute;left:0;bottom:0;width:1200px;height:100px;background:linear-gradient(180deg,var(--peach) 0%,var(--orange) 55%,var(--red) 100%)}
.hero-copy{position:absolute;left:582px;top:200px;width:520px}
.hero-copy h1{font-size:46px;line-height:1.15;font-weight:400}
.hero-copy p{font-size:20px;color:#555;margin-top:22px}
.more-btn{display:inline-block;margin-top:18px;background:var(--red);color:var(--white);font-size:13px;font-weight:700;padding:6px 16px}

/* story */
.story{position:absolute;top:700px;left:0;width:1200px;height:920px;background:var(--cream)}
.section-title{font-size:46px;font-weight:400}
.lead{font-size:14px;line-height:1.55;color:var(--text);margin-top:8px}
.doctor-banner{position:absolute;left:0;top:218px;width:980px;height:322px;background:linear-gradient(180deg,#c9d6dc 0%,#e4e9ea 55%,#d7d8d2 100%)}
.doctor-photo{position:absolute;right:40px;top:0;width:320px;height:322px;background:linear-gradient(180deg,#e9c9ac 0%,#8aa8c4 70%,#6d8fb0 100%)}
.doctor-name{position:absolute;left:120px;top:92px;font-family:"Source Sans 3",sans-serif;font-size:42px;line-height:1.1;color:var(--red);font-weight:600;white-space:nowrap}
.doctor-name span{font-weight:300;color:#555}
.doctor-sub{position:absolute;left:120px;top:150px;font-size:14px;color:#555}
.doctor-phone{position:absolute;left:120px;top:182px;background:var(--red);color:var(--white);font-size:20px;font-weight:600;padding:6px 18px;display:flex;gap:8px;align-items:center}
.cols{position:absolute;top:575px;left:0;width:980px;display:flex;gap:60px}
.cols > div{flex:1}
.cols h3{font-size:26px}

/* services */
.services{position:absolute;top:1620px;left:0;width:1200px;height:660px;background:linear-gradient(180deg,#ffffff 0%,#f8efe8 100%)}
.service-grid{position:absolute;top:150px;left:0;width:980px;display:grid;grid-template-columns:465px 465px;gap:14px 50px}
.service-card{position:relative;height:220px}
.service-card .photo{position:absolute;inset:0}
.service-label{position:absolute;left:14px;bottom:14px;display:flex;align-items:center;gap:12px}
.service-num{width:52px;height:52px;background:var(--orange);color:var(--white);font-size:30px;font-weight:700;display:flex;align-items:center;justify-content:center}
.service-label span{color:var(--white);font-weight:700;font-size:19px;line-height:1.15}
.slide-arrow{position:absolute;top:360px;width:30px;height:30px;border-radius:50%;background:#888;display:flex;align-items:center;justify-content:center}

/* contact */
.contact{position:absolute;top:2280px;left:0;width:1200px;height:736px;background:var(--white)}
.form-col{position:absolute;left:0;top:205px;width:420px}
.field-label{font-size:11px;font-weight:700;color:#555;letter-spacing:.5px}
.field-label b{color:var(--red)}
.field{width:420px;height:42px;border:1px solid #cfcfcf;margin:6px 0 22px}
.field.tall{height:145px}
.submit{margin-left:280px;background:var(--red);color:var(--white);font-weight:700;font-size:16px;padding:12px 28px;display:inline-block}
.address-col{position:absolute;left:500px;top:205px;width:480px}
.col-label{font-size:12px;font-weight:700;color:#555;letter-spacing:.5px}
.map{display:inline-block;width:150px;height:110px;background:linear-gradient(135deg,#e3e6e3,#cfd7d2);margin-top:14px;vertical-align:top}
.address-text{display:inline-block;margin:18px 0 0 20px;font-size:15px;color:#555;line-height:1.6}
.address-text .email{color:var(--red);font-size:12px}
.big-phone{font-size:36px;color:var(--red);margin-top:6px;display:flex;gap:10px;align-items:center;font-family:"Source Sans 3",sans-serif}

/* footer */
.site-footer{position:absolute;top:3016px;left:0;width:1200px;height:380px;background:var(--footer);border-top:10px solid var(--red)}
.footer-cols{position:absolute;left:110px;top:40px;width:980px;display:flex}
.footer-cols h4{font-size:13px;font-weight:700;color:#444;letter-spacing:.5px;margin-bottom:14px}
.footer-cols ul{list-style:none;font-size:12px;line-height:1.95;color:#666}
.sitemap{width:320px;display:flex;flex-wrap:wrap}
.sitemap h4{width:100%}
.sitemap ul{width:160px}
.hours{width:330px}
.hours li{display:flex;justify-content:space-between;width:240px}
.social-btns{display:flex;gap:12px;margin-bottom:14px}
.social-btn{background:#3b5b99;color:var(--white);font-size:13px;font-weight:600;padding:6px 14px;display:flex;align-items:center;gap:8px}
.social-btn.alt{background:#33a7d9}
.social-btn i{width:14px;height:14px;background:rgba(255,255,255,.85);display:inline-block}
.fine{font-size:11px;color:#777;line-height:1.6}
</style>
</head>
<body>

<section class="hero">
  <div class="hero-photo" role="img" aria-label="Smiling woman in a fitness top lifting small red dumbbells"></div>
  <div class="hero-band" role="img" aria-label="Decorative red and orange wave band"></div>
  <div class="hero-copy">
    <h1>Kelvaro Motion &amp; Orthopedic Physical Therapy</h1>
    <p>15 years of experience and dedication to physical rehabilitation</p>
    <span class="more-btn">LEARN MORE →</span>
  </div>
</section>

<header class="site-header">
  <div class="brand"><span class="brand-mark"></span><span class="brand-name">Kelvaro</span></div>
  <div class="header-phone">
    <svg width="16" height="16" viewBox="0 0 24 24" aria-hidden="true"><path fill="#c4272b" d="M6.6 10.8a15 15 0 0 0 6.6 6.6l2.2-2.2c.3-.3.7-.4 1-.2 1.1.4 2.3.6 3.6.6.6 0 1 .4 1 1V20c0 .6-.4 1-1 1A17 17 0 0 1 3 4c0-.6.4-1 1-1h3.5c.6 0 1 .4 1 1 0 1.3.2 2.5.6 3.6.1.3 0 .7-.2 1z"/></svg>
    555-014-2278
  </div>
  <span class="appt-btn">REQUEST AN APPOINTMENT</span>
  <nav class="main-nav"><span class="active">Home</span><span>Our Story</span><span>Services</span><span>Insurance</span><span>Contact</span></nav>
</header>

<section class="story">
  <div class="wrap" style="top:130px;height:780px">
    <h2 class="section-title">Our Story</h2>
    <p class="lead">Our services are the result of 15 years of experience of Dr. Dana Whitlock, PT, DPT, MS in sports and orthopedic physical therapy. Dana directed the rehabilitation services for the largest orthopedic group in Harlow County. She has provided care for athletes and active adults with injuries of the spine, shoulder, elbow, wrist, hand, hip, knee, ankle and foot. Her expertise is the treatment of sports and orthopedic injuries, whether they are the result of trauma, repetitive movements or the result of a surgical intervention.</p>
    <div class="doctor-banner" role="img" aria-label="Mountain landscape with a portrait of the lead physical therapist">
      <div class="doctor-photo" role="img" aria-label="Portrait of the lead physical therapist"></div>
      <div class="doctor-name">Dana Whitlock<span>, PT, DPT, MS</span></div>
      <div class="doctor-sub">Make an Appointment Call Dana</div>
      <div class="doctor-phone">
        <svg width="18" height="18" viewBox="0 0 24 24" aria-hidden="true"><path fill="#fff" d="M6.6 10.8a15 15 0 0 0 6.6 6.6l2.2-2.2c.3-.3.7-.4 1-.2 1.1.4 2.3.6 3.6.6.6 0 1 .4 1 1V20c0 .6-.4 1-1 1A17 17 0 0 1 3 4c0-.6.4-1 1-1h3.5c.6 0 1 .4 1 1 0 1.3.2 2.5.6 3.6.1.3 0 .7-.2 1z"/></svg>
        555-014-2278
      </div>
    </div>
    <div class="cols">
      <div>
        <h3>Our Approach</h3>
        <p class="lead">Our services are the result of 15 years of experience of Dr. Dana Whitlock, PT, DPT, MS in sports and orthopedic physical therapy. Dana directed the rehabilitation services for the largest orthopedic group in Harlow County. She has provided care for sports and orthopedic injuries of the spine, shoulder, elbow, wrist, hand, hip, knee, ankle and foot.</p>
      </div>
      <div>
        <h3>Mission &amp; Vision</h3>
        <p class="lead">Her expertise is the treatment of all sports and orthopedic injuries, whether they are the result of trauma, repetitive movements or the result of a surgical intervention.</p>
      </div>
    </div>
  </div>
</section>

<section class="services">
  <div class="wrap" style="top:45px;height:600px">
    <h2 class="section-title">Services</h2>
    <p class="lead">Our services are the result of 15 years of experience of Dr. Dana Whitlock, PT, DPT, MS in sports and orthopedic physical therapy. Dana directed the rehabilitation services for the largest orthopedic group in Harlow County, and she has provided care for athletes of every level.</p>
    <div class="service-grid">
      <div class="service-card">
        <div class="photo" role="img" aria-label="Therapist treating a patient's leg" style="background:linear-gradient(135deg,#2d5f86,#d9a27d 60%,#3b6d94)"></div>
        <div class="service-label"><span class="service-num">1</span><span>Sports Medicine<br>Rehabilitation</span></div>
      </div>
      <div class="service-card">
        <div class="photo" role="img" aria-label="Therapist guiding a patient through an exercise" style="background:linear-gradient(135deg,#4a3a33,#9c7a66 55%,#33434f)"></div>
        <div class="service-label"><span class="service-num">2</span><span>Orthopedic Injury<br>Rehabilitation</span></div>
      </div>
      <div class="service-card">
        <div class="photo" role="img" aria-label="Patient doing a balance exercise in the clinic" style="background:linear-gradient(135deg,#c9a487,#e6b89a 50%,#6c5b52)"></div>
        <div class="service-label"><span class="service-num">3</span><span>Preoperative<br>Rehabilitation</span></div>
      </div>
      <div class="service-card">
        <div class="photo" role="img" aria-label="Patient doing a spine stretching exercise" style="background:linear-gradient(135deg,#1f5b73,#3b8aa3 50%,#c58f6f)"></div>
        <div class="service-label"><span class="service-num">4</span><span>Spine<br>Rehabilitation</span></div>
      </div>
    </div>
  </div>
  <div class="slide-arrow" style="left:40px"><svg width="12" height="12" viewBox="0 0 12 12" aria-hidden="true"><path d="M8 1 L3 6 L8 11" stroke="#fff" stroke-width="2" fill="none"/></svg></div>
  <div class="slide-arrow" style="left:1130px"><svg width="12" height="12" viewBox="0 0 12 12" aria-hidden="true"><path d="M4 1 L9 6 L4 11" stroke="#fff" stroke-width="2" fill="none"/></svg></div>
</section>

<section class="contact">
  <div class="wrap" style="top:30px;height:700px">
    <h2 class="section-title">Contact Us</h2>
    <p class="lead">Our services are the result of 15 years of experience of Dr. Dana Whitlock, PT, DPT, MS in sports and orthopedic physical therapy. Dana directed the rehabilitation services for the largest orthopedic group in Harlow County. Reach out and we will reply within one day.</p>
    <div class="form-col">
      <div class="field-label">NAME <b>*</b></div><div class="field"></div>
      <div class="field-label">EMAIL <b>*</b></div><div class="field"></div>
      <div class="field-label">MESSAGE <b>*</b></div><div class="field tall"></div>
      <span class="submit">SUBMIT</span>
    </div>
    <div class="address-col">
      <div class="col-label">ADDRESS</div>
      <div class="map" role="img" aria-label="Street map showing the clinic location"></div>
      <div class="address-text">218 Orchard Lane<br>Suite 4, Brookfield PA<br><span class="email">Email ✉</span><br><span class="email">dwhitlock@kelvaromotionrx.com</span></div>
      <div class="col-label" style="margin-top:60px">PHONE NUMBER:</div>
      <div class="big-phone">
        <svg width="30" height="30" viewBox="0 0 24 24" aria-hidden="true"><path fill="#c4272b" d="M6.6 10.8a15 15 0 0 0 6.6 6.6l2.2-2.2c.3-.3.7-.4 1-.2 1.1.4 2.3.6 3.6.6.6 0 1 .4 1 1V20c0 .6-.4 1-1 1A17 17 0 0 1 3 4c0-.6.4-1 1-1h3.5c.6 0 1 .4 1 1 0 1.3.2 2.5.6 3.6.1.3 0 .7-.2 1z"/></svg>
        555-014-2278
      </div>
    </div>
  </div>
</section>

<footer class="site-footer">
  <div class="footer-cols">
    <div class="sitemap">
      <h4>SITEMAP</h4>
      <ul><li>Home</li><li>Location</li><li>News</li><li>Our Story</li><li>Mission Statement</li><li>Services</li></ul>
      <ul><li>Insurance</li><li>New Patients</li><li>Contact Us</li><li>Testimonials</li><li>Community</li></ul>
    </div>
    <div class="hours">
      <h4>OUR OFFICE HOURS</h4>
      <ul><li><span>Monday</span><span>7am - 7pm</span></li><li><span>Tuesday</span><span>7am - 7pm</span></li><li><span>Wednesday</span><span>7am - 7pm</span></li><li><span>Thursday</span><span>7am - 7pm</span></li><li><span>Friday</span><span>7am - 5pm</span></li></ul>
    </div>
    <div>
      <h4>GET SOCIAL WITH US</h4>
      <div class="social-btns"><span class="social-btn"><i></i>Like Us</span><span class="social-btn alt"><i></i>Follow Us</span></div>
      <p class="fine">© Kelvaro Motion &amp; Orthopedic Physical Therapy<br>Terms of use Privacy Policy</p>
    </div>
  </div>
</footer>

</body>
</html>
```